Business Card Design for Event Planning Company

Create a business card for event planning company using our new logo. After I pick the design, I will need files made for 6 employees. Our company provides event design & logistics services as well as venue management. The font should be sans serif and complementary to the logo. I will need to know the name of the font selected for the final design. The phone numbers listed should be separated by "." not "-"

Address for the card
PO Box 318, Washington, DC 20019

Card One
Lorna Pettibone
lpettibone@galavoyant.com
202.481.7730

Card Two
Miriam Okonkwo
mokonkwo@galavoyant.com
202.556.2047

Card Three
Tessa Varnholt
tvarnholt@galavoyant.com
978.620.4471

Card Four
Robin Fess
rfess@galavoyant.com
202.718.3362

Card Five
Ada-Rose Pelletan-Uzor
adarose@galavoyant.com
202.839.1205

Card Six
Beatrix Holloway
Beatrix@galavoyant.com
202.492.6618

Target Market(s)

Corporate/Non-Profit

Industry/Entity Type

Event Planning

Contact Information for Business Card

Address for the card

Card One
Lorna Pettibone
lpettibone@galavoyant.com
202.481.7730

Card Two
Miriam Okonkwo
202.556.2047

Card Three
Tessa Varnholt
978.620.4471

Card Four
Robin Fess
rfess@galavoyant.com
202.718.3362

Card Five
Ada-Rose Pelletan-Uzor
202.839.1205

Card Six
Beatrix Holloway
202.492.6618

Font styles to use
Sans Serif

Colors

Designer to choose colors to be used in the design.

Requirements
Must have
• Two-sided with logo
Should not have
• Extra colors or be too busy

```html
<!DOCTYPE html>
<html lang="en">
<head>
<meta charset="utf-8">
<title>Galavoyant Business Card</title>
<link rel="stylesheet" href="https://fonts.googleapis.com/css2?family=Open+Sans:wght@300;400;700&display=swap">
<style>
  :root {
    --page-bg: #e4e2df;
    --card-face: #efeeec;
    --teal: #5aa6a5;
    --edge-ink: #1c1b1b;
    --light-text: #ffffff;
    --brand-ink: #2a2728;
  }
  * { box-sizing: border-box; margin: 0; padding: 0; }
  html, body {
    width: 1200px;
    height: 900px;
    overflow: hidden;
    background: var(--page-bg);
    font-family: "Open Sans", Arial, sans-serif;
  }
  .business-card {
    position: absolute;
    left: 150px;
    top: 171px;
    width: 900px;
    height: 557px;
    background: var(--card-face);
    box-shadow: 0 10px 30px rgba(0,0,0,0.12);
    overflow: hidden;
  }
  .card-shape {
    position: absolute;
    inset: 0;
  }
  .holder-name {
    position: absolute;
    left: 50px;
    top: 68px;
    color: var(--light-text);
    font-weight: 700;
    font-size: 35px;
    letter-spacing: 0.5px;
    text-transform: uppercase;
  }
  .postal-address {
    position: absolute;
    left: 50px;
    top: 305px;
    color: var(--light-text);
    font-style: normal;
    font-weight: 400;
    font-size: 22px;
    line-height: 36px;
  }
  .contact-list {
    position: absolute;
    left: 50px;
    top: 402px;
    list-style: none;
    color: var(--light-text);
    font-size: 22px;
    line-height: 33px;
  }
  .contact-item {
    display: flex;
    align-items: center;
    gap: 12px;
  }
  .contact-icon {
    width: 17px;
    height: 17px;
    flex: none;
  }
  .brand-name {
    position: absolute;
    left: 412px;
    width: 470px;
    top: 244px;
    text-align: center;
    color: var(--brand-ink);
    font-weight: 300;
    font-size: 58px;
    letter-spacing: 1px;
  }
</style>
</head>
<body>
  <section class="business-card">
    <svg class="card-shape" width="900" height="557" viewBox="0 0 900 557" aria-hidden="true">
      <path d="M0 0 H491 C472 120 390 235 294 272 C390 305 470 420 482 557 H0 Z" fill="var(--teal)"/>
      <path d="M491 0 C472 120 390 235 294 272 C390 305 470 420 482 557" fill="none" stroke="var(--edge-ink)" stroke-width="5"/>
    </svg>

    <h1 class="holder-name">Lorna Pettibone</h1>

    <address class="postal-address">
      PO Box 318,<br>Washington, DC 20019
    </address>

    <ul class="contact-list">
      <li class="contact-item">
        <svg class="contact-icon" viewBox="0 0 24 24" aria-hidden="true"><path fill="#fff" d="M6.6 10.8a15.2 15.2 0 0 0 6.6 6.6l2.2-2.2c.3-.3.7-.4 1-.2 1.1.4 2.3.6 3.6.6.6 0 1 .4 1 1V20c0 .6-.4 1-1 1C10.6 21 3 13.4 3 4c0-.6.4-1 1-1h3.5c.6 0 1 .4 1 1 0 1.3.2 2.5.6 3.6.1.3 0 .7-.2 1z"/></svg>
        <span>202.481.7730</span>
      </li>
      <li class="contact-item">
        <svg class="contact-icon" viewBox="0 0 24 24" aria-hidden="true"><path fill="#fff" d="M2 5h20v14H2z"/><path fill="none" stroke="var(--teal)" stroke-width="1.8" d="M2.5 5.5 12 13l9.5-7.5"/></svg>
        <span>lpettibone@galavoyant.com</span>
      </li>
      <li class="contact-item">
        <svg class="contact-icon" viewBox="0 0 24 24" aria-hidden="true"><circle cx="12" cy="12" r="10" fill="#fff"/><path fill="none" stroke="var(--teal)" stroke-width="1.6" d="M2 12h20M12 2c3 3 3 17 0 20M12 2c-3 3-3 17 0 20"/></svg>
        <span>www.galavoyant.com</span>
      </li>
    </ul>

    <p class="brand-name">galavoyant</p>
  </section>
</body>
</html>
```